Paul Whitcombe's FIG cat Art Gallery catalog

i want create a 5.5 x 8.5 8 page catalog to promote my artwork.. have included pics of an old one and have sketched out layout and order for the 8 pages.. i have my house which is a work in progress and have included the before and after pic and have kind of strategically placed the images in a certain order.. i have been included in print and tv for rvnb , belmont east, coastal hearth...and have included their trademarked logo however I'm not sure if i can print these but was thinking that the designer could put a BOLD TYPE FONT..in the BIO which kind of highlights my involvement etc... but will include my rough sketches and want to make this a fun creative self promotion piece etc...thanks! and please email with any questions etc

Target Market(s)

custom customers

Industry/Entity Type

Artists

Font styles to use
Serif

Requirements
Must have
• 8 pages and the images that i have included.. with all info and please leave room under each artwork for the title of the artwork.
• please make sure that the designer is ABLE to convert ALL files into print ready form
Nice to have
• want it to showcase the art and would love to have a similar feel of the red and green catalog that i've attached pic
• may have a simple classical serif type font but am open to designers suggestions....the bio copy should be easy to read plain probably no serif
• front cover would be nice to have a bright lemon yellow with logo on top and bottom half could be a bright med blueish aqua to royal blue...water feel.. since I'm in florida.

```html
<!DOCTYPE html>
<html lang="en">
<head>
<meta charset="utf-8">
<title>FIG cat Art Gallery – Catalog Spread</title>
<link rel="stylesheet" href="https://fonts.googleapis.com/css2?family=Gelasio:wght@400;500&family=Open+Sans:ital,wght@0,400;0,600;0,700;1,400&display=swap">
<style>
  :root {
    --paper: #f4f4f4;
    --ink: #111111;
    --accent-red: #d3243a;
    --lemon: #fde910;
    --lemon-deep: #f2c40d;
    --royal: #1d4f9a;
    --aqua: #5a8fd6;
    --band-blue: #1f5a97;
    --muted: #444444;
  }
  * { box-sizing: border-box; margin: 0; padding: 0; }
  html, body {
    width: 1200px; height: 833px; overflow: hidden;
    background: #9a9a9a;
  }
  .spread {
    position: relative;
    width: 1200px; height: 833px;
    display: flex;
  }
  .page { position: relative; width: 600px; height: 833px; overflow: hidden; }

  /* ---------- Back cover (left) ---------- */
  .back-cover { background: var(--paper); }
  .intro {
    position: absolute; left: 40px; top: 60px; width: 280px;
    text-align: center;
  }
  .brand-title {
    font-family: "Gelasio", serif; font-weight: 400;
    font-size: 34px; letter-spacing: 0.3px; color: var(--ink);
    white-space: nowrap;
  }
  .established {
    font-family: "Open Sans", sans-serif; font-size: 13px;
    color: var(--accent-red); margin-top: 4px;
  }
  .bio {
    margin-top: 30px; text-align: left;
    font-family: "Open Sans", sans-serif; font-style: italic;
    font-size: 13.5px; line-height: 1.25; color: var(--ink);
  }
  .quote {
    margin-top: 38px;
    font-family: "Open Sans", sans-serif; font-size: 21px; line-height: 1.35;
    color: var(--ink);
  }
  .quote-author {
    margin-top: 18px;
    font-family: "Open Sans", sans-serif; font-size: 21px; color: var(--ink);
  }
  .social-small {
    margin-top: 16px;
    font-family: "Open Sans", sans-serif; font-size: 11px; color: var(--muted);
  }
  .featured-artwork {
    position: absolute; left: 340px; top: 0; width: 260px; height: 728px;
    background:
      radial-gradient(circle at 55% 40%, #c98a4a 0%, #a8663a 22%, transparent 45%),
      radial-gradient(circle at 40% 85%, #1d7a6e 0%, transparent 40%),
      radial-gradient(circle at 80% 15%, #14163f 0%, transparent 45%),
      linear-gradient(180deg, #2a3f9b 0%, #3a2f7a 35%, #b54333 65%, #1c4f8f 100%);
  }
  .contact-band {
    position: absolute; left: 0; bottom: 0; width: 600px; height: 105px;
    background: var(--lemon);
  }
  .keep-in-touch {
    position: absolute; left: 0; bottom: 0; width: 170px; height: 150px;
    background: var(--band-blue); border-top-right-radius: 150px;
    padding: 50px 0 0 22px;
    font-family: "Open Sans", sans-serif; font-weight: 700;
    font-size: 27px; line-height: 1.25; color: #ffffff;
  }
  .contact-item {
    position: absolute; display: flex; align-items: center; gap: 12px;
    font-family: "Open Sans", sans-serif; font-size: 13px; color: var(--ink);
    white-space: nowrap;
  }
  .contact-icon {
    width: 24px; height: 24px; border-radius: 50%; background: #ffffff;
    display: flex; align-items: center; justify-content: center; flex: none;
  }
  .contact-phone { left: 190px; top: 738px; }
  .contact-web { left: 285px; top: 768px; }
  .contact-address { right: 10px; top: 798px; }

  /* ---------- Front cover (right) ---------- */
  .front-cover { background: var(--royal); }
  .sky-half {
    position: absolute; left: 0; top: 0; width: 600px; height: 440px;
    background:
      radial-gradient(ellipse at 30% 30%, #fff36b 0%, transparent 55%),
      radial-gradient(ellipse at 80% 70%, var(--lemon-deep) 0%, transparent 60%),
      var(--lemon);
  }
  .water-half {
    position: absolute; left: 0; top: 440px; width: 600px; height: 393px;
    background:
      radial-gradient(ellipse at 30% 60%, var(--aqua) 0%, transparent 55%),
      radial-gradient(ellipse at 75% 30%, #2c66b8 0%, transparent 60%),
      linear-gradient(180deg, var(--royal) 0%, #2a63b4 100%);
  }
  .horizon {
    position: absolute; left: 0; top: 432px; width: 600px; height: 16px;
  }
  .gallery-name {
    position: absolute; left: 150px; top: 340px; width: 300px;
    display: flex; align-items: center; gap: 14px; justify-content: center;
  }
  .gallery-name .mark {
    width: 40px; height: 40px; border-radius: 50%; background: var(--ink); flex: none;
  }
  .gallery-name span {
    font-family: "Open Sans", sans-serif; font-weight: 700;
    font-size: 24px; line-height: 1.15; color: var(--ink);
  }
  .social-large {
    position: absolute; right: 24px; bottom: 30px;
    font-family: "Open Sans", sans-serif; font-weight: 600;
    font-size: 13px; color: #ffffff; display: flex; gap: 16px;
  }
</style>
</head>
<body>
<main class="spread">

  <section class="page back-cover">
    <div class="intro">
      <h1 class="brand-title">Whitcombe Studio</h1>
      <p class="established">Est. 1965</p>
      <p class="bio">Lorem ipsum dolor sit amet, consectetuer adipiscing elit, sed diam nonummy nibh euismod tincidunt ut laoreet dolore magna aliquam erat volutpat. Ut wisi enim ad minim veniam, quis nostrud exerci tation ullamcorper suscipit lobortis nisl ut aliquip ex ea commodo consequat. Duis autem vel eum iriure dolor in hendrerit in vulputate velit esse molestie consequat, vel illum dolore eu feugiat nulla facilisis at vero eros et accumsan et iusto odio dignissim qui blandit praesent luptatum zzril delenit augue duis dolore te feugait nulla facilisi.</p>
      <p class="quote">"...Art should awaken the senses."</p>
      <p class="quote-author">-Paul Whitcombe-</p>
      <p class="social-small">Picstream · Viewtube</p>
    </div>

    <div class="featured-artwork" role="img" aria-label="Featured painting: a colourful portrait of a dog with red flowers and dotted patterns"></div>

    <div class="contact-band"></div>
    <div class="keep-in-touch">Keep in<br>Touch</div>

    <div class="contact-item contact-phone">
      <span class="contact-icon">
        <svg width="14" height="14" viewBox="0 0 24 24"><path fill="#1f5a97" d="M6.6 10.8a15 15 0 0 0 6.6 6.6l2.2-2.2c.3-.3.7-.4 1-.2 1.1.4 2.3.6 3.6.6.6 0 1 .4 1 1V20c0 .6-.4 1-1 1A17 17 0 0 1 3 4c0-.6.4-1 1-1h3.5c.6 0 1 .4 1 1 0 1.3.2 2.5.6 3.6.1.3 0 .7-.2 1z"/></svg>
      </span>
      012 . 555. 0148
    </div>
    <div class="contact-item contact-web">
      <span class="contact-icon">
        <svg width="14" height="14" viewBox="0 0 24 24" fill="none" stroke="#1f5a97" stroke-width="2"><circle cx="12" cy="12" r="9"/><path d="M3 12h18M12 3c3 3.5 3 14.5 0 18M12 3c-3 3.5-3 14.5 0 18"/></svg>
      </span>
      www.figcatart.com
    </div>
    <div class="contact-item contact-address">
      <span class="contact-icon">
        <svg width="14" height="14" viewBox="0 0 24 24"><path fill="#1f5a97" d="M12 2a7 7 0 0 0-7 7c0 5 7 13 7 13s7-8 7-13a7 7 0 0 0-7-7zm0 9.5A2.5 2.5 0 1 1 12 6.5a2.5 2.5 0 0 1 0 5z"/></svg>
      </span>
      4410 Palm Row, Tampa, FL 33602
    </div>
  </section>

  <section class="page front-cover">
    <div class="sky-half" role="img" aria-label="Painted lemon-yellow sky texture"></div>
    <div class="water-half" role="img" aria-label="Painted blue water texture"></div>
    <svg class="horizon" viewBox="0 0 600 16" preserveAspectRatio="none">
      <path d="M0 8 C150 5 300 10 450 7 S600 8 600 8" stroke="#111" stroke-width="3" fill="none"/>
      <path d="M0 11 C200 9 350 13 600 10" stroke="#111" stroke-width="1.5" fill="none"/>
    </svg>
    <div class="gallery-name">
      <span class="mark"></span>
      <span>Paul Whitcombe's<br>FIG cat Art Gallery</span>
    </div>
    <div class="social-large"><span>Picstream</span><span>Viewtube</span></div>
  </section>

</main>
</body>
</html>
```